Business Card - Existing Logo & Branding copied to Business Card Format

We are looking for a designer to help with designing a two sided business card for us. We sell a web based software platform that helps people sell access to online training.
We have an existing logo and recently completed a design project here on draft hive to have someone design a nice trade show booth for us (also attached file for that design as well as our logo). We really like the look and feel of the tradeshow booth design. The fonts, colors, etc all work for us. We are hoping someone can create something very similar just in business card format.
Should be pretty straight forward hopefully....
On one side we want the logo, employee name, email address, phone and fax. On the other side we would like the text "transform your organizations training, revenue products = revenue" - See the attached PSD for what we want that to look like.
You can also see our website at www.tutorvane.com for an example of our branding.
We are open to ideas, have done several projects on draft hive and love when designers come up with creative approaches that are even better then what we envisioned.
Software

```html
<!DOCTYPE html>
<html lang="en">
<head>
<meta charset="utf-8">
<title>TutorVane Business Card</title>
<link rel="stylesheet" href="https://fonts.googleapis.com/css2?family=Jost:wght@400;600&family=Zilla+Slab:wght@700&display=swap">
<style>
  :root {
    --brand-red: #b0101a;
    --ink: #111214;
    --charcoal: #2b2f33;
    --paper: #ffffff;
    --front-light: #f1f1f1;
    --front-mid: #d9d9d9;
    --bulb-light: #f4f4f4;
    --bulb-mid: #dcdcdc;
  }
  html, body {
    margin: 0;
    padding: 0;
    width: 1200px;
    height: 1000px;
    overflow: hidden;
    background: var(--paper);
  }
  .canvas {
    position: relative;
    width: 1200px;
    height: 1000px;
    background: var(--paper);
    font-family: "Jost", sans-serif;
  }
  .card {
    position: absolute;
    box-sizing: border-box;
    overflow: hidden;
  }
  .card--front {
    left: 173px;
    top: 90px;
    width: 679px;
    height: 387px;
    background: radial-gradient(ellipse at 50% 45%, var(--front-light) 0%, var(--front-mid) 100%);
    border: 1px solid #e4e4e4;
  }
  .brand-lockup {
    position: absolute;
    left: 56px;
    top: 144px;
    display: flex;
    align-items: center;
    gap: 26px;
  }
  .brand-square {
    width: 106px;
    height: 96px;
    background: var(--brand-red);
  }
  .brand-name {
    font-family: "Jost", sans-serif;
    font-weight: 600;
    font-size: 84px;
    line-height: 1;
    color: var(--charcoal);
    letter-spacing: -1px;
  }
  .card--back {
    left: 340px;
    top: 518px;
    width: 680px;
    height: 390px;
    background: var(--paper);
    border: 1px solid #e6e6e6;
  }
  .bulb-art {
    position: absolute;
    left: 395px;
    top: 18px;
    width: 265px;
    height: 372px;
    background: linear-gradient(180deg, var(--bulb-light) 0%, var(--bulb-mid) 100%);
    border-radius: 130px 130px 40px 40px;
    opacity: 0.7;
  }
  .back-brand {
    position: absolute;
    right: 24px;
    top: 34px;
    font-family: "Jost", sans-serif;
    font-weight: 600;
    font-size: 22px;
    color: var(--brand-red);
  }
  .holder-name {
    position: absolute;
    left: 33px;
    top: 98px;
    margin: 0;
    font-family: "Zilla Slab", serif;
    font-weight: 700;
    font-size: 48px;
    letter-spacing: 2px;
    color: var(--brand-red);
  }
  .contact {
    position: absolute;
    left: 33px;
    top: 166px;
    margin: 0;
    font-style: normal;
    font-size: 28px;
    line-height: 37px;
    color: var(--ink);
  }
  .contact p { margin: 0; }
  .contact .address { margin-top: 11px; }
</style>
</head>
<body>
<main class="canvas">
  <section class="card card--front" aria-label="Card front">
    <div class="brand-lockup">
      <div class="brand-square"></div>
      <span class="brand-name">TutorVane</span>
    </div>
  </section>

  <section class="card card--back" aria-label="Card back">
    <div class="bulb-art" role="img" aria-label="Faint sketched light bulb illustration"></div>
    <span class="back-brand">TutorVane</span>
    <h1 class="holder-name">Dana Reyes</h1>
    <address class="contact">
      <p>info@tutorvane.com</p>
      <p>800.410.2291</p>
      <p>Fax: 800.555.014</p>
      <div class="address">
        <p>1187 NW Alder St #318</p>
        <p>Portland, OR 97209</p>
      </div>
    </address>
  </section>
</main>
</body>
</html>
```